Business cards and stationary for a health and wellbeing company
Lumen Forms
Business cards and stationary for a health and wellbeing company - Health
Creative Brief
Bright & Fun-filled
Jolene prescott
Director
PO Box
sales@lumenforms.com.au
www.lumenforms.com.au
Hi, I am happy to have a wide selection of fonts and designs. Lumen Forms is a health conscious Australian business that sells protein, supplements, health equipment, meditation and beauty products. We pride ourselves on great customer service, great products and a true passion for feeling and looking good. Our target market is females aged 18-60 years of age, mums and woman who want to feel amazing. Colour • Pink • White • Blue • Purple
Im open to different designs.
JolenePrescott JolenePrescott
Hi Everyone, Thank you so much for your great designs! I love the bright colours and lines that flow rather than straight and sharp. Could you please show me the front as well as the back of the business cards. I am wanting to change the font on my logo? I am wanting it so that the word Lumen sits above the word forms. Looking forward to some great designs! Thanks!

```html
<!DOCTYPE html>
<html lang="en">
<head>
<meta charset="utf-8">
<title>Lumen Forms — Business Cards</title>
<link href="https://fonts.googleapis.com/css2?family=Nunito:wght@400;600;800&display=swap" rel="stylesheet">
<style>
  :root {
    --backdrop: #ecebe8;
    --card: #ffffff;
    --card-shade: #eeeeef;
    --purple: #a43c9f;
    --magenta: #d2329b;
    --cyan: #22b4e6;
    --ink: #4a4a4a;
    --rule: #9a9a9a;
  }
  * { box-sizing: border-box; margin: 0; padding: 0; }
  html, body {
    width: 1200px; height: 901px; overflow: hidden;
    background: var(--backdrop);
    font-family: "Nunito", sans-serif;
  }
  .canvas { position: relative; width: 1200px; height: 901px; }
  .card {
    position: absolute; left: 320px; width: 560px; height: 320px;
    background: linear-gradient(135deg, var(--card) 0%, var(--card) 55%, var(--card-shade) 100%);
    border-radius: 4px; overflow: hidden;
    box-shadow: 0 10px 26px rgba(0,0,0,.18);
  }
  .card-front { top: 110px; }
  .card-back { top: 470px; }

  /* Front */
  .front-brand {
    position: absolute; left: 150px; top: 140px;
    display: flex; align-items: center; gap: 16px;
  }
  .front-dot {
    width: 48px; height: 48px; border-radius: 50%; background: var(--purple);
  }
  .front-name {
    font-weight: 800; font-size: 44px; letter-spacing: -1px; line-height: 1;
    color: var(--purple);
  }

  /* Back */
  .brand {
    position: absolute; left: 38px; top: 70px;
    display: flex; align-items: center; gap: 10px;
  }
  .brand-dot {
    width: 34px; height: 34px; border-radius: 50%; background: var(--purple);
  }
  .brand-name {
    font-weight: 800; font-size: 26px; letter-spacing: -.5px; color: var(--purple);
  }
  .divider {
    position: absolute; left: 290px; top: 34px; width: 1px; height: 120px;
    background: var(--rule);
  }
  .contact {
    position: absolute; left: 302px; top: 36px;
    list-style: none; font-size: 13px; line-height: 1.35; color: var(--ink);
  }
  .contact li { display: flex; align-items: center; gap: 6px; margin-bottom: 4px; }
  .contact .address { display: block; }
  .contact svg { flex: none; }
  .wave { position: absolute; left: 0; top: 0; width: 560px; height: 320px; }
  .holder {
    position: absolute; left: 0; bottom: 12px; width: 100%; text-align: center;
    color: #fff; font-size: 13px; letter-spacing: 2px; font-weight: 600;
  }
  .holder .role { font-weight: 400; letter-spacing: 1px; }
</style>
</head>
<body>
<main class="canvas">

  <section class="card card-front" aria-label="Card front">
    <div class="front-brand">
      <span class="front-dot" aria-hidden="true"></span>
      <p class="front-name">Lumen Forms</p>
    </div>
  </section>

  <section class="card card-back" aria-label="Card back">
    <svg class="wave" viewBox="0 0 560 320" aria-hidden="true">
      <defs>
        <linearGradient id="bandFill" x1="0" y1="0" x2="1" y2="0">
          <stop offset="0" stop-color="#9b3ea6"/>
          <stop offset="1" stop-color="#d2329b"/>
        </linearGradient>
      </defs>
      <path d="M0 222 C150 262 330 210 560 170 L560 200 C330 238 150 282 0 250 Z" fill="#bfe9f8"/>
      <path d="M0 214 C150 254 330 200 560 160" fill="none" stroke="var(--cyan)" stroke-width="5"/>
      <path d="M0 250 C150 282 330 238 560 200 L560 320 L0 320 Z" fill="url(#bandFill)"/>
    </svg>

    <div class="brand">
      <span class="brand-dot" aria-hidden="true"></span>
      <span class="brand-name">Lumen Forms</span>
    </div>

    <div class="divider" aria-hidden="true"></div>
    <ul class="contact">
      <li class="address">PO Box 412, Pelham<br>Queensland Road QLD</li>
      <li>
        <svg width="11" height="11" viewBox="0 0 12 12" aria-hidden="true"><path d="M2 1 L4.5 1 L5.5 3.5 L4 4.5 C4.8 6.2 5.8 7.2 7.5 8 L8.5 6.5 L11 7.5 L11 10 C11 10.6 10.6 11 10 11 C5 11 1 7 1 2 C1 1.4 1.4 1 2 1 Z" fill="var(--cyan)"/></svg>
        012 555 0147
      </li>
      <li>
        <svg width="12" height="10" viewBox="0 0 12 10" aria-hidden="true"><rect x="0.5" y="0.5" width="11" height="9" rx="1" fill="var(--cyan)"/><path d="M1 1 L6 5.5 L11 1" fill="none" stroke="#fff" stroke-width="1.2"/></svg>
        sales@lumenforms.com.au
      </li>
      <li>
        <svg width="11" height="11" viewBox="0 0 12 12" aria-hidden="true"><circle cx="6" cy="6" r="5.5" fill="var(--cyan)"/><path d="M0.5 6 H11.5 M6 0.5 C3 3 3 9 6 11.5 M6 0.5 C9 3 9 9 6 11.5" fill="none" stroke="#fff" stroke-width="0.9"/></svg>
        www.lumenforms.com.au
      </li>
    </ul>

    <p class="holder">JOLENE PRESCOTT <span class="role">Director</span></p>
  </section>

</main>
</body>
</html>
```